Vantrel

I already have a website created through Plovix.com - https://vantrel.co.nz.

Its an accounting services business, can get ideas from tzhl.co.nz, fwu.co.nz, yrx.co.nz

I would like to have this recreated using coding. I need the following features and functionalities incorporated:

- Live Chat feature
- Moving Carousel feature for Reviews
- Advanced SEO support (Google Analytics)

Industry/Entity Type

accounting

Coding

Coded - Design and coding required

Number of Pages Required

5+ page

```html
<!DOCTYPE html>
<html lang="en">
<head>
<meta charset="utf-8">
<title>Vantrel – Our Services</title>
<link href="https://fonts.googleapis.com/css2?family=Montserrat:wght@800&family=Roboto:wght@300;400;500;700&display=swap" rel="stylesheet">
<style>
:root{
  --ink:#3d4a4f;
  --text:#4a4a4a;
  --muted:#6b6b6b;
  --soft:#a5a5a5;
  --teal:#8fb9ae;
  --teal-band:#93bbb0;
  --teal-bright:#8fd6c2;
  --line:#e6e6e6;
  --white:#ffffff;
  --hero-a:#2f414b;
  --hero-b:#6b7a80;
}
*{margin:0;padding:0;box-sizing:border-box}
html,body{width:1200px;height:3750px;overflow:hidden}
body{position:relative;background:var(--white);font-family:"Roboto",Arial,sans-serif;color:var(--text)}
.abs{position:absolute}

.top-strip{left:0;top:0;width:1200px;height:9px;background:var(--ink)}
.site-header{left:0;top:9px;width:1200px;height:74px;background:var(--white)}
.brand{position:absolute;left:69px;top:18px;display:flex;align-items:center;gap:8px;color:var(--teal);font-weight:700;font-size:17px;letter-spacing:2px}
.brand-dot{width:22px;height:22px;border-radius:50%;background:var(--teal)}
.main-nav{position:absolute;left:420px;top:28px;display:flex;gap:22px;font-size:12px;color:#333}
.consult{position:absolute;left:945px;top:0;width:194px;height:74px;background:var(--teal);color:var(--white);display:flex;align-items:center;padding-left:18px;gap:12px}
.consult small{display:block;font-size:9px;opacity:.9}
.consult strong{display:block;font-size:15px;font-weight:500;letter-spacing:.5px}

.hero{left:0;top:83px;width:1200px;height:377px;background:linear-gradient(120deg,var(--hero-a) 0%,#4b5e68 45%,var(--hero-b) 75%,#3c4c55 100%)}
.hero h1{position:absolute;left:73px;top:150px;font-family:"Montserrat",Arial,sans-serif;font-weight:800;font-size:64px;color:var(--white);letter-spacing:.5px}

.section-title{position:absolute;left:0;width:1200px;text-align:center;font-size:38px;font-weight:300;color:#333}
.section-title b{font-weight:700}
.section-sub{position:absolute;left:0;width:1200px;text-align:center;font-size:13px;line-height:19px;color:var(--muted);font-weight:300}

.card{position:absolute;width:275px;height:203px;border:3px solid #ececec;background:var(--white);text-align:center;padding:34px 16px 0}
.card svg{width:40px;height:40px;display:block;margin:0 auto}
.card h3{margin-top:14px;font-size:13px;font-weight:500;color:#333}
.card p{margin-top:10px;font-size:10px;line-height:15px;color:var(--muted)}

.wide-card{position:absolute;left:460px;top:1727px;width:574px;height:205px;border:3px solid #ececec;background:var(--white)}
.acc-mark{position:absolute;left:50px;top:26px;width:130px;text-align:center}
.acc-square{width:70px;height:70px;background:#1fa9cf;margin:0 auto 10px}
.acc-name{font-size:15px;font-weight:700;color:#2b2b2b;line-height:17px}
.acc-copy{position:absolute;left:220px;top:62px;width:330px}
.acc-copy h3{font-size:22px;font-weight:400;color:#333}
.acc-copy p{margin-top:4px;font-size:15px;line-height:22.5px;color:#444;font-weight:300}

.banner{left:0;top:2024px;width:1200px;height:358px;background:linear-gradient(110deg,#2c3a41 0%,#46565d 50%,#34444b 100%);text-align:center}
.banner h2{position:absolute;left:0;top:105px;width:1200px;font-size:45px;font-weight:500;color:var(--teal-bright);letter-spacing:.5px}
.banner p{position:absolute;left:0;top:154px;width:1200px;font-size:19px;line-height:28px;color:var(--white)}
.btn-outline{position:absolute;border:1.5px solid var(--white);color:var(--white);font-size:13px;display:flex;align-items:center;justify-content:center}

.certified h2{position:absolute;left:111px;top:2486px;font-size:51px;line-height:61px;color:#333;font-weight:300}
.certified h2 b{font-weight:500}
.certified p{position:absolute;left:111px;top:2640px;width:550px;font-size:13.5px;line-height:19.5px;color:#444}
.team-photo{left:772px;top:2458px;width:307px;height:346px;border-radius:12px;background:linear-gradient(140deg,#e9ecef 0%,#c9d3db 45%,#5d7590 100%)}
.cert-badge{left:753px;top:2659px;width:170px;height:151px;background:var(--white);border-radius:12px;display:flex;align-items:center;justify-content:center}
.cert-badge span{width:90px;height:90px;background:#2d9fd8;border-radius:14px}

.cta-band{left:0;top:2873px;width:1200px;height:138px;background:var(--teal-band)}
.cta-band p{position:absolute;left:73px;top:42px;font-size:22px;line-height:31px;color:var(--white)}

.review{position:absolute;top:3276px;width:275px;height:284px;border:3px solid #ececec;background:var(--white);text-align:center;padding:64px 24px 0}
.avatar{position:absolute;top:3224px;width:92px;height:92px;border-radius:50%;border:3px solid var(--white);background:radial-gradient(circle at 50% 40%,#c8a48d 0%,#7a6a63 60%,#3b4d63 100%)}
.review h4{font-size:13px;font-weight:500;color:#333}
.review .role{font-size:12px;color:var(--soft);margin-top:6px}
.review .stars{margin-top:6px;display:flex;justify-content:center;gap:2px}
.review .stars svg{width:15px;height:15px}
.review p{margin-top:8px;font-size:10px;line-height:15px;color:#555}
.arrow{position:absolute;top:3367px;width:50px;height:50px;border-radius:50%;background:var(--teal);display:flex;align-items:center;justify-content:center}

.chat{left:1096px;top:3620px;width:68px;height:62px}
.site-footer{left:0;top:3676px;width:1200px;height:74px;background:var(--ink)}
.site-footer small{position:absolute;left:65px;top:28px;font-size:12px;color:var(--white)}
.social{position:absolute;top:22px;width:28px;height:28px;border-radius:50%;border:1.5px solid var(--white)}
</style>
</head>
<body>

<svg width="0" height="0" style="position:absolute">
  <defs>
    <symbol id="ico-doc" viewBox="0 0 40 40"><rect x="8" y="4" width="22" height="30" rx="2" fill="none" stroke="#333" stroke-width="2"/><rect x="12" y="22" width="3" height="8" fill="#333"/><rect x="17" y="18" width="3" height="12" fill="#333"/><rect x="22" y="14" width="3" height="16" fill="#333"/><line x1="12" y1="10" x2="26" y2="10" stroke="#333" stroke-width="2"/></symbol>
    <symbol id="ico-coin" viewBox="0 0 40 40"><circle cx="14" cy="14" r="9" fill="none" stroke="#333" stroke-width="2"/><text x="14" y="18" font-size="11" text-anchor="middle" fill="#333" font-family="Arial">$</text><rect x="20" y="26" width="3" height="10" fill="#333"/><rect x="25" y="20" width="3" height="16" fill="#333"/><rect x="30" y="14" width="3" height="22" fill="#333"/></symbol>
    <symbol id="ico-person" viewBox="0 0 40 40"><circle cx="16" cy="12" r="6" fill="none" stroke="#333" stroke-width="2"/><path d="M5 34c0-8 5-13 11-13s11 5 11 13" fill="none" stroke="#333" stroke-width="2"/><path d="M30 20l4-8 2 2" fill="none" stroke="#333" stroke-width="2"/></symbol>
    <symbol id="ico-grid" viewBox="0 0 40 40"><rect x="6" y="6" width="28" height="28" rx="2" fill="none" stroke="#333" stroke-width="2"/><rect x="6" y="6" width="14" height="28" fill="#333"/><line x1="20" y1="15" x2="34" y2="15" stroke="#333" stroke-width="2"/><line x1="20" y1="24" x2="34" y2="24" stroke="#333" stroke-width="2"/></symbol>
    <symbol id="ico-star" viewBox="0 0 24 24"><path d="M12 2l3 7 7 .6-5.4 4.7 1.7 7.2L12 17.8 5.7 21.5l1.7-7.2L2 9.6 9 9z" fill="#111"/></symbol>
  </defs>
</svg>

<div class="abs top-strip"></div>
<header class="abs site-header">
  <div class="brand"><span class="brand-dot"></span>VANTREL</div>
  <nav class="main-nav"><span>HOME</span><span>SERVICES</span><span>ABOUT US</span><span>PRICING</span><span>CONTACT US</span></nav>
  <div class="consult">
    <svg width="44" height="34" viewBox="0 0 44 34"><rect x="2" y="2" width="26" height="18" rx="3" fill="none" stroke="#fff" stroke-width="2"/><rect x="14" y="12" width="26" height="16" rx="3" fill="var(--teal)" stroke="#fff" stroke-width="2"/><line x1="19" y1="18" x2="35" y2="18" stroke="#fff" stroke-width="1.5"/><line x1="19" y1="23" x2="31" y2="23" stroke="#fff" stroke-width="1.5"/></svg>
    <div><small>Get Consultation</small><strong>020 555 0143</strong></div>
  </div>
</header>

<section class="abs hero" role="img" aria-label="Photo of hands using a calculator over paperwork">
  <h1>OUR ERVICES</h1>
</section>

<h2 class="section-title" style="top:523px">OUR <b>SERVICES</b></h2>
<p class="section-sub" style="top:580px">We offer a comprehensive suite of accounting services to ensure your&nbsp; organization's<br>financial operations run smoothly and efficiently.</p>

<div class="card" style="left:146px;top:661px"><svg><use href="#ico-doc"/></svg><h3>Monthly Reporting</h3><p>Regular, detailed financial reports that give you a clear view of your financial position at all times. From profit and loss statements to cash flow and balance sheets, our reporting is tailored to your needs.</p></div>
<div class="card" style="left:456px;top:661px"><svg><use href="#ico-doc"/></svg><h3>Annual Financial Statements</h3><p>Preparation of financial statements in line with IFRS/PBE audit-compliant standards for transparency and accountability.</p></div>
<div class="card" style="left:764px;top:661px"><svg><use href="#ico-coin"/></svg><h3>Cash Flow Reporting</h3><p>Accurate forecasting and monitoring of your cash flow to ensure liquidity and financial stability.</p></div>

<div class="card" style="left:146px;top:927px"><svg><use href="#ico-doc"/></svg><h3>Budgets &amp; Forecasts</h3><p>Regular, detailed financial reports that give you a clear view of your&nbsp; financial position at all times. From profit and loss statements</p></div>
<div class="card" style="left:456px;top:927px"><svg><use href="#ico-doc"/></svg><h3>GST, PAYE</h3><p>Regular, detailed financial reports that give you a clear view of your&nbsp; financial position at all times. From profit and loss statements</p></div>
<div class="card" style="left:764px;top:927px"><svg><use href="#ico-coin"/></svg><h3>Financial Performance &amp; Analysis</h3><p>In-depth analysis to track profitability, identify trends, and support strategic decisions.</p></div>

<div class="card" style="left:146px;top:1194px"><svg><use href="#ico-coin"/></svg><h3>Payroll</h3><p>Complete payroll management, ensuring timely and compliant processing of employee payments.</p></div>
<div class="card" style="left:462px;top:1194px"><svg><use href="#ico-person"/></svg><h3>Business Development Advice</h3><p>Expert guidance on financial growth, performance improvement, and sustainable business strategies.</p></div>
<div class="card" style="left:764px;top:1194px"><svg><use href="#ico-doc"/></svg><h3>TRA &amp; Audit Compliance</h3><p>Ensuring that your organization meets all TRA tax obligations and audit standards.</p></div>

<div class="card" style="left:146px;top:1460px"><svg><use href="#ico-doc"/></svg><h3>Project Accounting</h3><p>Project based accounting support such as reconciliations, rectifying historical transactions, recoding and balance date transition.</p></div>
<div class="card" style="left:462px;top:1460px"><svg><use href="#ico-grid"/></svg><h3>Gridcalc Templates</h3><p>Tailored, user-friendly Gridcalc templates to streamline financial reporting and analysis.</p></div>
<div class="card" style="left:764px;top:1460px"><svg><use href="#ico-coin"/></svg><h3>Ledgra Setup &amp; Training</h3><p>Professional setup and hands-on training for Ledgra, LedgraMe, empowering you to manage&nbsp; your finances with confidence and efficiency.</p></div>

<div class="card" style="left:146px;top:1727px"><svg><use href="#ico-doc"/></svg><h3>Audits</h3><p>Tailored audit and financial review services for Tier 3 and Tier 4 charitable trusts with annual expenditure under $550,000.</p></div>
<div class="wide-card">
  <div class="acc-mark"><div class="acc-square"></div><div class="acc-name">REGISTERED<br>ACCOUNTANTS</div></div>
  <div class="acc-copy"><h3>As Registered Accountants</h3><p>we bring extensive expertise and a personalised approach to help your organisation navigate its financial&nbsp; responsibilities with confidence.</p></div>
</div>

<section class="abs banner" role="img" aria-label="Photo of a desk with financial charts, a tablet and a pen">
  <h2>THESE SERVICES ARE DESIGNED</h2>
  <p>to support your financial health,&nbsp; compliance, and long-term growth, while delivering high-quality outcomes<br>through expertknowledge and innovative tools.</p>
  <span class="btn-outline" style="left:533px;top:240px;width:133px;height:34px">Contact Us Today</span>
</section>

<section class="certified">
  <h2>We are proud to be<br><b>Ledgra Advisor Certified</b></h2>
  <p>Providing cloud-based accounting solutions that streamline your financial&nbsp; processes while ensuring accuracy and compliance. Whether you're looking for help with financial reporting, budgeting, grant management, or tax&nbsp; filings, our dedicated team is here to support your growth and success.&nbsp; We're committed to helping you navigate the complexities of accounting,&nbsp; allowing you to focus on what truly matters—achieving your mission and objectives.</p>
  <div class="abs team-photo" role="img" aria-label="Photo of two colleagues reviewing charts on a laptop"></div>
  <div class="abs cert-badge"><span></span></div>
</section>

<section class="abs cta-band">
  <p>I look forward to working alongside you to<br>support your organisation's financial health and future growth.</p>
  <span class="btn-outline" style="left:957px;top:58px;width:134px;height:35px">Contact Us Today</span>
</section>

<h2 class="section-title" style="top:3078px">WHAT'S <b>OUR CLIENT SAY</b></h2>
<p class="section-sub" style="top:3136px">We offer a comprehensive suite of accounting services to ensure your&nbsp; organization's<br>financial operations run smoothly and efficiently.</p>

<div class="review" style="left:157px"><h4>Mara T. Ellison</h4><div class="role">Designation</div><div class="stars"><svg><use href="#ico-star"/></svg><svg><use href="#ico-star"/></svg><svg><use href="#ico-star"/></svg><svg><use href="#ico-star"/></svg><svg><use href="#ico-star"/></svg></div><p>The point of using Lorem Ipsum is that it has a more-or-less normal distribution of letters, as opposed to using 'Content here, content here', making it look like readable English. Many desktop publishing packages and web page editors now use Lorem Ipsum</p></div>
<div class="review" style="left:467px"><h4>Mara T. Ellison</h4><div class="role">Designation</div><div class="stars"><svg><use href="#ico-star"/></svg><svg><use href="#ico-star"/></svg><svg><use href="#ico-star"/></svg><svg><use href="#ico-star"/></svg><svg><use href="#ico-star"/></svg></div><p>The point of using Lorem Ipsum is that it has a more-or-less normal distribution of letters, as opposed to using 'Content here, content here', making it look like readable English. Many desktop publishing packages and web page editors now use Lorem Ipsum</p></div>
<div class="review" style="left:778px"><h4>Mara T. Ellison</h4><div class="role">Designation</div><div class="stars"><svg><use href="#ico-star"/></svg><svg><use href="#ico-star"/></svg><svg><use href="#ico-star"/></svg><svg><use href="#ico-star"/></svg><svg><use href="#ico-star"/></svg></div><p>The point of using Lorem Ipsum is that it has a more-or-less normal distribution of letters, as opposed to using 'Content here, content here', making it look like readable English. Many desktop publishing packages and web page editors now use Lorem Ipsum</p></div>

<div class="avatar" style="left:249px" role="img" aria-label="Client portrait photo"></div>
<div class="avatar" style="left:558px" role="img" aria-label="Client portrait photo"></div>
<div class="avatar" style="left:869px" role="img" aria-label="Client portrait photo"></div>

<div class="arrow" style="left:83px"><svg width="16" height="16" viewBox="0 0 16 16"><path d="M10 2L4 8l6 6" fill="none" stroke="#fff" stroke-width="1.6"/></svg></div>
<div class="arrow" style="left:1077px"><svg width="16" height="16" viewBox="0 0 16 16"><path d="M6 2l6 6-6 6" fill="none" stroke="#fff" stroke-width="1.6"/></svg></div>

<svg class="abs chat" viewBox="0 0 68 62" aria-label="Live chat">
  <path d="M34 4C16 4 4 14 4 28c0 9 5 16 13 20l-3 11 12-8c3 .6 5 .8 8 .8 18 0 30-10 30-24S52 4 34 4z" fill="#a8d5c8"/>
  <circle cx="22" cy="28" r="5" fill="#fff"/><circle cx="34" cy="28" r="5" fill="#fff"/><circle cx="46" cy="28" r="5" fill="#fff"/>
</svg>

<footer class="abs site-footer">
  <small>© 2025 VANTREL.CO.NZ. ALL RIGHTS RESERVED</small>
  <span class="social" style="left:996px"></span>
  <span class="social" style="left:1034px"></span>
  <span class="social" style="left:1071px"></span>
</footer>

</body>
</html>
```